We are a Leadership Specialist Boutique Business that is launching a residential womans workshop....

We need a post card which will include our logo, an overview of our workshop, a catch statement on one side and on the other side dates, venue, facilitators and contacts to book the workshop. The postcards will be distributed at an Global Sisterhood Harvest Lunch. They will be placed at each setting of the lunch attendees. The company QBR running the lunch is a sponsor of our business.

Target Market(s)

Women supervisor to middle management positions or own business

Industry/Entity Type

Academic Training

Font styles to use
Serif

Colors
34a7d8

Requirements
Must have
• Use Colour Palette on docs attached, Logo, Workshop overview either the Circle Theory or the Core Philosophy Text,
• The dates, venue, all costs of the program including discount code. One catch sentence that grabs the audience from the content I have provided that appeals to the designer
• Must have these contacts.
• Website: brightpathforwardgroup.com,au
• Email: Info@brightpathforwardgroup.com.au.
• Phone: 0419372605
Nice to have
• Facilitators Photos and names

```html
<!DOCTYPE html>
<html lang="en">
<head>
<meta charset="utf-8">
<title>Bright Path Forward – Residential Workshop Postcard</title>
<link rel="stylesheet" href="https://fonts.googleapis.com/css2?family=Quicksand:wght@500;700&display=swap">
<style>
  :root{
    --mint:#b3e1dc;
    --mint-light:#c9ece7;
    --blue:#34a7d8;
    --blue-deep:#1e8fc8;
    --ink:#111111;
    --grey-text:#333333;
    --paper:#ffffff;
    --stage:#ececec;
  }
  *{margin:0;padding:0;box-sizing:border-box}
  html,body{width:1200px;height:973px;overflow:hidden}
  body{background:var(--stage);font-family:"Quicksand",sans-serif;color:var(--ink);position:relative}
  .postcard{position:absolute;top:290px;width:560px;height:394px;overflow:hidden;box-shadow:0 2px 8px rgba(0,0,0,.25)}
  .postcard--front{left:30px;background:var(--mint)}
  .postcard--back{left:610px;background:var(--paper)}
  .postcard svg.shapes{position:absolute;inset:0;width:100%;height:100%}
  .photo-area{position:absolute;inset:0}

  .brand-name{position:absolute;font-weight:700;color:var(--ink);text-align:center;line-height:1.05}
  .postcard--front .brand-name{left:30px;top:178px;width:140px;font-size:22px}
  .postcard--back .brand-name{left:18px;top:90px;width:110px;font-size:16px}

  .headline{position:absolute;right:50px;top:22px;text-align:right;font-weight:700;line-height:1}
  .headline .line-1{font-size:44px;letter-spacing:-.5px}
  .headline .line-1 .lead{font-weight:500}
  .headline .line-2{font-size:36px;margin-top:8px}
  .headline .line-2 .lead{font-weight:500}

  .contact{position:absolute;right:50px;top:130px;text-align:right;font-weight:700}
  .contact .email{font-size:15px}
  .contact .phone{font-size:38px;line-height:1;margin-top:2px;letter-spacing:1px}
  .contact .web{font-size:14.5px;margin-top:2px}

  .details{position:absolute;right:287px;top:138px;text-align:right;width:252px}
  .details .label{font-size:11px;font-weight:700;color:var(--grey-text);line-height:1.15}
  .details .tag{display:inline-block;background:var(--blue);color:var(--paper);font-size:10.5px;font-weight:700;padding:0 3px;line-height:1.3;margin-top:1px}
  .details .tag .light{font-weight:500}
  .details .group{margin-bottom:5px}
  .details p.overview{font-size:7px;font-weight:500;line-height:1.2;text-align:justify;text-align-last:right;color:var(--grey-text);margin-top:2px}
  .details p.overview + p.overview{margin-top:4px}

  .price-row{position:absolute;left:0;bottom:0;display:flex;gap:6px}
  .price{width:100px;height:56px;background:var(--mint);text-align:center}
  .price:nth-child(2){width:84px}
  .price:nth-child(3){width:71px}
  .price .amount{background:var(--blue);color:var(--paper);font-weight:700;font-size:20px;line-height:24px}
  .price .note{font-size:7.5px;font-weight:700;color:var(--grey-text);line-height:1.1;margin-top:2px}
  .price .note strong{display:block;font-size:15px;line-height:1}
  .price .note .big{font-size:14px}
  .price .note-only{font-size:15px;font-weight:700;color:var(--grey-text);margin-top:3px}

  .stamp-box{position:absolute;left:460px;top:20px;width:81px;height:82px;border:1px solid var(--ink)}
</style>
</head>
<body>

<section class="postcard postcard--front" aria-label="Postcard front">
  <svg class="shapes" viewBox="0 0 560 394" aria-hidden="true">
    <path d="M0 0 H300 Q140 35 0 130 Z" fill="var(--mint-light)"/>
  </svg>
  <svg class="photo-area" viewBox="0 0 560 394" role="img" aria-label="Photo of women joining hands together in a circle">
    <defs>
      <linearGradient id="photoTone" x1="0" y1="0" x2="1" y2="0.3">
        <stop offset="0" stop-color="#8c8f99"/>
        <stop offset="0.45" stop-color="#d9c9cc"/>
        <stop offset="0.75" stop-color="#ef8fbd"/>
        <stop offset="1" stop-color="#d93b8d"/>
      </linearGradient>
    </defs>
    <path d="M0 270 Q280 205 560 218 V394 H0 Z" fill="url(#photoTone)"/>
  </svg>
  <svg class="shapes" viewBox="0 0 560 394" aria-hidden="true">
    <path d="M0 238 Q300 175 560 180 V222 Q300 205 0 280 Z" fill="var(--blue)"/>
    <path d="M0 255 Q300 200 560 205 V222 Q300 210 0 280 Z" fill="var(--blue-deep)" opacity=".35"/>
    <circle cx="100" cy="205" r="100" fill="var(--mint)"/>
    <path d="M13 255 A100 100 0 0 1 150 118" fill="none" stroke="var(--blue)" stroke-width="8"/>
  </svg>
  <div class="brand-name">Bright Path Forward</div>
  <div class="headline">
    <div class="line-1"><span class="lead">The</span> core philosophy</div>
    <div class="line-2"><span class="lead">of the</span> program</div>
  </div>
  <div class="contact">
    <div class="email">Info@brightpathforwardgroup.com.au</div>
    <div class="phone">0419372605</div>
    <div class="web">brightpathforwardgroup.com.au</div>
  </div>
</section>

<section class="postcard postcard--back" aria-label="Postcard back">
  <svg class="shapes" viewBox="0 0 560 394" aria-hidden="true">
    <path d="M0 0 H80 Q200 40 320 62 Q470 88 531 157 Q430 100 280 96 Q120 96 0 190 Z" fill="var(--mint)"/>
    <path d="M0 200 Q60 130 200 110 Q420 86 531 157 Q420 115 260 120 Q120 128 0 225 Z" fill="var(--blue)"/>
    <circle cx="73" cy="107" r="72" fill="var(--mint)"/>
    <path d="M11 145 A72 72 0 0 1 111 46" fill="none" stroke="var(--blue)" stroke-width="6"/>
  </svg>
  <div class="brand-name">Bright Path Forward</div>
  <div class="stamp-box" aria-label="Stamp area"></div>
  <div class="details">
    <div class="group">
      <div class="label">Program and<br>Upcoming Dates</div>
      <span class="tag">2 ½ Days <span class="light">residential</span></span><br>
      <span class="tag">26th <span class="light">to</span> 28th May 2019</span>
    </div>
    <div class="group">
      <div class="label">May Venue</div>
      <span class="tag"><span class="light">The Ridgeline Lodge, Kurrajong NSW</span></span>
    </div>
    <div class="group">
      <div class="label">Future Programs</div>
      <span class="tag">August, October, March</span>
    </div>
    <p class="overview">The program is emersive and wholistic which includes development of your life and leadership skills, by rewriting your narrative and a personal action plan for change Support &amp; Program Inclusions</p>
    <p class="overview">LPQ Assessment, leadership skills sessions, individual coaching sessions, guest speakers, body wellness therapists as well as accomodation and all meals are included Investment for May 2019 Program</p>
  </div>
  <div class="price-row">
    <div class="price">
      <div class="amount">$3,495</div>
      <div class="note">Early Bird Book by<strong>26th April</strong></div>
    </div>
    <div class="price">
      <div class="amount">$3,095</div>
      <div class="note">Quote QBR Code<br><span class="big">9455</span> for a further</div>
    </div>
    <div class="price">
      <div class="amount">$100</div>
      <div class="note-only">Discount</div>
    </div>
  </div>
</section>

</body>
</html>
```